All-natural soap packaging design for new company

The box type has been selected, we just need artwork for each of our 10 products. I'd like the same look to each, the idea is just to switch out the name and ingredient label on each. The dimensions are 3.5"x3.75"x1.25". The colors in the uploaded pictures with product titles are not mandatory. I'd like to keep the font on the packaging (Rubik) as it is the same as the website.

Target Market(s)

Health & Beauty, people looking for natural or organic products

Industry/Entity Type

It Company

Colors

Designer to choose colors to be used in the design.

Requirements
Must have
• Design must be clean and relatively simple. Slightly different look for each of the 10 products. Audience is people looking for all-natural products.

```html
<!DOCTYPE html>
<html lang="en">
<head>
<meta charset="utf-8">
<title>Ashby Soap Co. – Recipe No. 6</title>
<link href="https://fonts.googleapis.com/css2?family=Rubik:wght@300;400;500&family=Saira+Extra+Condensed:wght@400&display=swap" rel="stylesheet">
<style>
  :root {
    --backdrop: #d3e1e7;
    --kraft: #c49a68;
    --kraft-deep: #b88c5c;
    --violet: #4e3794;
    --violet-band: #523b98;
    --lavender: #8f7ccc;
    --lavender-soft: #b3a6de;
    --white: #ffffff;
  }
  html, body {
    margin: 0;
    width: 1200px;
    height: 1200px;
    overflow: hidden;
    background: var(--backdrop);
  }
  .box-front {
    position: absolute;
    left: 150px;
    top: 180px;
    width: 900px;
    height: 840px;
    background: radial-gradient(ellipse at 50% 40%, var(--kraft) 0%, var(--kraft-deep) 100%);
    overflow: hidden;
  }
  .brand {
    position: absolute;
    top: 80px;
    left: 0;
    right: 0;
    display: flex;
    flex-direction: column;
    align-items: center;
    gap: 18px;
  }
  .brand-square {
    width: 120px;
    height: 120px;
    background: var(--violet);
  }
  .brand-name {
    font-family: "Rubik", sans-serif;
    font-weight: 500;
    font-size: 26px;
    letter-spacing: 1px;
    color: var(--violet);
    text-transform: uppercase;
  }
  .recipe-title {
    position: absolute;
    top: 290px;
    left: 0;
    right: 0;
    margin: 0;
    text-align: center;
    font-family: "Saira Extra Condensed", sans-serif;
    font-weight: 400;
    font-size: 78px;
    line-height: 1;
    color: var(--violet);
    letter-spacing: 1px;
  }
  .lavender-field {
    position: absolute;
    left: 0;
    right: 0;
    top: 400px;
    bottom: 0;
    background: linear-gradient(to bottom, rgba(143,124,204,0) 0%, rgba(143,124,204,0.55) 35%, var(--lavender-soft) 60%, var(--lavender) 100%);
  }
  .flavour-band {
    position: absolute;
    left: 0;
    right: 0;
    top: 590px;
    height: 170px;
    background: var(--violet-band);
    display: flex;
    align-items: center;
    justify-content: flex-end;
    padding-right: 40px;
    box-sizing: border-box;
  }
  .flavour-name {
    margin: 0;
    font-family: "Rubik", sans-serif;
    font-weight: 300;
    font-size: 44px;
    line-height: 1.1;
    color: var(--white);
    text-align: right;
    text-transform: uppercase;
  }
</style>
</head>
<body>
  <main class="box-front">
    <div class="lavender-field" role="img" aria-label="Illustrated sprigs of lavender growing along the bottom of the box"></div>
    <div class="brand">
      <div class="brand-square"></div>
      <div class="brand-name">Ashby Soap Co.</div>
    </div>
    <h1 class="recipe-title">RECIPE NO. 6</h1>
    <div class="flavour-band">
      <p class="flavour-name">Lavender<br>+ Witch Hazel</p>
    </div>
  </main>
</body>
</html>
```